Re-design of Business Card

We require a design for our business card.

Korrim is a supplier of industrial packaging specializing in plastic products. We are undergoing a rebranding to appear more corporate. We have changed our company name to korrim and have a new logo.

I have uploaded our old card design with the previous company name.
Don't copy the current design. We are looking for a new design.

Industry/Entity Type

Manufacturing

Contact Information for Business Card

please don't copy the current design. we are looking for a new design.

Font styles to use
Sans Serif

Colors

Designer to choose colors to be used in the design.

Requirements
Must have
• clean and easy to read.

```html
<!DOCTYPE html>
<html lang="en">
<head>
<meta charset="utf-8">
<title>Korrim Business Card</title>
<link rel="stylesheet" href="https://fonts.googleapis.com/css2?family=Montserrat:wght@700;800&family=Hind:wght@400&family=Roboto+Condensed:wght@300&display=swap">
<style>
  :root {
    --orange: #f37d21;
    --charcoal: #333333;
    --white: #ffffff;
    --ink: #2b2b2b;
    --backdrop: #ececec;
  }
  * { margin: 0; padding: 0; box-sizing: border-box; }
  html, body {
    width: 1200px;
    height: 1200px;
    overflow: hidden;
    background: var(--backdrop);
  }
  .canvas {
    position: relative;
    width: 1200px;
    height: 1200px;
  }
  .card {
    position: absolute;
    left: 190px;
    width: 820px;
    height: 533px;
    border-radius: 31px;
    overflow: hidden;
    box-shadow: 0 6px 18px rgba(0,0,0,0.18);
  }

  /* Back of card */
  .card-back {
    top: 38px;
    background: linear-gradient(90deg, var(--orange) 0 50%, var(--charcoal) 50% 100%);
  }
  .back-wordmark {
    position: absolute;
    left: 0; right: 0;
    top: 190px;
    text-align: center;
    font-family: "Montserrat", sans-serif;
    font-weight: 800;
    font-size: 118px;
    letter-spacing: 4px;
    color: var(--white);
    line-height: 1;
  }
  .back-tagline {
    position: absolute;
    left: 42px;
    bottom: 38px;
    font-family: "Montserrat", sans-serif;
    font-weight: 800;
    font-size: 22px;
    color: var(--white);
  }

  /* Front of card */
  .card-front {
    top: 621px;
    background: var(--white);
  }
  .front-wordmark {
    position: absolute;
    left: 100px;
    top: 193px;
    width: 272px;
    height: 99px;
    display: flex;
    align-items: center;
    justify-content: center;
    font-family: "Montserrat", sans-serif;
    font-weight: 800;
    font-size: 56px;
    letter-spacing: 2px;
    color: var(--orange);
  }
  .name-block {
    position: absolute;
    left: 412px;
    top: 64px;
    width: 408px;
    height: 111px;
    background: var(--orange);
    padding: 14px 0 0 26px;
    color: var(--white);
  }
  .person-name {
    font-family: "Montserrat", sans-serif;
    font-weight: 800;
    font-size: 34px;
    line-height: 1.1;
  }
  .person-title {
    font-family: "Hind", sans-serif;
    font-weight: 400;
    font-size: 27px;
    line-height: 1.5;
  }
  .contact-rule {
    position: absolute;
    left: 412px;
    top: 175px;
    width: 6px;
    height: 198px;
    background: var(--orange);
  }
  .contact-list {
    position: absolute;
    left: 438px;
    top: 196px;
    width: 362px;
    list-style: none;
  }
  .contact-item {
    display: flex;
    align-items: center;
    height: 48px;
    font-family: "Roboto Condensed", sans-serif;
    font-weight: 300;
    font-size: 27px;
    letter-spacing: -0.2px;
    white-space: nowrap;
    color: var(--ink);
  }
  .contact-icon {
    width: 30px;
    height: 30px;
    margin-right: 14px;
    flex: none;
  }
  .address {
    position: absolute;
    left: 128px;
    top: 428px;
    display: flex;
    align-items: center;
    font-family: "Roboto Condensed", sans-serif;
    font-weight: 300;
    font-size: 27px;
    letter-spacing: -0.2px;
    white-space: nowrap;
    color: var(--ink);
  }
  .address .contact-icon {
    width: 18px;
    height: 24px;
    margin-right: 14px;
  }
  .footer-band {
    position: absolute;
    left: 0;
    bottom: 0;
    width: 820px;
    height: 32px;
  }
</style>
</head>
<body>
<main class="canvas">

  <section class="card card-back" aria-label="Card back">
    <div class="back-wordmark">KORRIM</div>
    <div class="back-tagline">Supplier of industrial packaging</div>
  </section>

  <section class="card card-front" aria-label="Card front">
    <div class="front-wordmark">KORRIM</div>

    <div class="name-block">
      <div class="person-name">Declan Moore</div>
      <div class="person-title">Machinery Sales Manager</div>
    </div>
    <div class="contact-rule"></div>

    <ul class="contact-list">
      <li class="contact-item">
        <svg class="contact-icon" viewBox="0 0 30 30" aria-hidden="true">
          <rect x="8" y="3" width="14" height="8" fill="none" stroke="#2b2b2b" stroke-width="1.8"/>
          <rect x="2" y="11" width="26" height="11" rx="2" fill="none" stroke="#2b2b2b" stroke-width="1.8"/>
          <rect x="7" y="17" width="16" height="10" fill="#fff" stroke="#2b2b2b" stroke-width="1.8"/>
          <line x1="10" y1="21" x2="20" y2="21" stroke="#2b2b2b" stroke-width="1.4"/>
          <line x1="10" y1="24" x2="20" y2="24" stroke="#2b2b2b" stroke-width="1.4"/>
        </svg>
        1300 481 206
      </li>
      <li class="contact-item">
        <svg class="contact-icon" viewBox="0 0 30 30" aria-hidden="true">
          <path d="M10 3 L13 9 L10.5 11.5 C11.5 15 14 19.5 17 21.5 L19.5 19.5 L24 24 L21 27 C13 26 6 15 6.5 6 Z" fill="#2b2b2b"/>
        </svg>
        07 3184 6620
      </li>
      <li class="contact-item">
        <svg class="contact-icon" viewBox="0 0 30 30" aria-hidden="true">
          <rect x="2" y="6" width="26" height="19" fill="none" stroke="#2b2b2b" stroke-width="2.2"/>
          <path d="M2 6 L15 17 L28 6 M2 25 L11.5 14 M28 25 L18.5 14" fill="none" stroke="#2b2b2b" stroke-width="2"/>
        </svg>
        sales@harlowpacking.com.au
      </li>
      <li class="contact-item">
        <svg class="contact-icon" viewBox="0 0 30 30" aria-hidden="true">
          <circle cx="15" cy="15" r="12.5" fill="none" stroke="#2b2b2b" stroke-width="1.8"/>
          <ellipse cx="15" cy="15" rx="5.5" ry="12.5" fill="none" stroke="#2b2b2b" stroke-width="1.6"/>
          <line x1="2.5" y1="15" x2="27.5" y2="15" stroke="#2b2b2b" stroke-width="1.6"/>
          <line x1="15" y1="2.5" x2="15" y2="27.5" stroke="#2b2b2b" stroke-width="1.6"/>
          <path d="M5 8.5 H25 M5 21.5 H25" stroke="#2b2b2b" stroke-width="1.4"/>
        </svg>
        www.korrim.com.au
      </li>
    </ul>

    <div class="address">
      <svg class="contact-icon" viewBox="0 0 18 24" aria-hidden="true">
        <path d="M9 1 C4.5 1 1.5 4.3 1.5 8.5 C1.5 14 9 23 9 23 C9 23 16.5 14 16.5 8.5 C16.5 4.3 13.5 1 9 1 Z" fill="#2b2b2b"/>
        <circle cx="9" cy="8.5" r="2.8" fill="#fff"/>
      </svg>
      48 Tallis St Meadowbrook, Qld 4131 Australia
    </div>

    <svg class="footer-band" viewBox="0 0 820 32" aria-hidden="true">
      <polygon points="60,0 412,0 412,32 34,32" fill="#f37d21"/>
      <polygon points="412,0 765,0 791,32 412,32" fill="#333333"/>
    </svg>
  </section>

</main>
</body>
</html>
```